Branding for Velēra Cider a new Tasmanian cider company

We are a new Tasmanian cider business looking for a logo/label design to be used on our 330ml cider bottle labels and as a logo.
We want our cider label to pop and stand out from the rest.
As our cider is a Tasmanian product we would like it to appear as a premium product.
I have attached pictures of all of the other Tasmanian Cider labels to give an idea of what we are competing with NOT because we like the designs!!!

We are yet to start advertising our business so it is all an open slab, we have no starting point just a few ideas that have been listed below in the "Nice to Haves" section.

This brief has been updated as what we originally requested was too similar to other labels already in production so didn't give our product an edge.

The label size will be approx 80mm x 125mm

Target Market(s)

Craft cider market, bottle shops, boutique bars and restaurants

Font styles to use
Serif
Decorative
Script

Colors

Designer to choose colors to be used in the design.

Requirements
Must have
• The words
• "Velēra Cider" with the diacritic's over the o's
• "Tasmanian Made"
• or
• "Made in Tasmania"
• The Tasmanian part can be in all caps if it looks better
Nice to have
• All or some of the below incorporated into the label:
• Velēra was the goddess of fruit trees, gardens, and orchards.
• She watched over and protected fruit trees
• She was thought to be a wood nymph which are usually represented as beautiful, young girls.
• We would like our label to possibly incorporate the above.
• Maybe a wood nymph/goddess in an apple/pear orchard or against an apple/pear tree.
• Maybe no tree, just the nymph/goddess holding fruit.
• Maybe an apple/pear branch with a nympy/goddess under it.
• I have attached a few images from searchly of wood nymphs and fruit goddess' for inspiration. Not sure if realistic or animated would look best, but if animated, not cartoon like as we would like a premium look. Possibly similar to the attached Torvik Cider artwork
• We will have 3 types of cider; Apple, Pear and Apple & Strawberry so essentially 3 labels, maybe the apple tree could change to a pear tree and for the apple & strawberry cider maybe strawberries growing under the apple tree?
• All just ideas, we are open to :)
• If you think something else will suit the name, please feel free to submit it

```html
<!DOCTYPE html>
<html lang="en">
<head>
<meta charset="utf-8">
<title>Velēra Cider – Label Range</title>
<link href="https://fonts.googleapis.com/css2?family=Cinzel:wght@700&family=Cormorant+Garamond:wght@500;600&display=swap" rel="stylesheet">
<style>
  :root {
    --board: #f2f2f2;
    --label-bg: #f2f2f2;
    --frame: #333333;
    --title: #2e2e2e;
    --pear: #a86a10;
    --apple: #3f5e0f;
    --strawberry: #b01a22;
  }
  html, body {
    margin: 0;
    padding: 0;
    width: 1200px;
    height: 1200px;
    overflow: hidden;
    background: var(--board);
  }
  .board {
    position: relative;
    width: 1200px;
    height: 1200px;
  }
  .label {
    position: absolute;
    width: 262px;
    height: 406px;
    box-sizing: border-box;
    border: 5px solid var(--frame);
    background: var(--label-bg);
    font-family: "Cormorant Garamond", Georgia, serif;
    font-weight: 600;
    color: var(--accent);
  }
  .label--pear { left: 48px; top: 97px; --accent: var(--pear); }
  .label--apple { left: 648px; top: 97px; --accent: var(--apple); }
  .label--strawberry { left: 340px; top: 697px; --accent: var(--strawberry); }

  .label__fruit {
    position: absolute;
    left: 50%;
    transform: translateX(-50%);
    top: 46px;
    width: 140px;
    height: 170px;
  }
  .label--pear .label__fruit {
    width: 110px;
    background: radial-gradient(circle at 40% 60%, #f1d21c 0%, #d9a817 55%, #b98a1a 100%);
    border-radius: 45% 45% 50% 50% / 35% 35% 65% 65%;
  }
  .label--apple .label__fruit {
    background: radial-gradient(circle at 38% 40%, #b8e85a 0%, #7cc62c 55%, #4f9a1c 100%);
    border-radius: 48%;
    height: 160px;
  }
  .label--strawberry .label__fruit {
    width: 128px;
    background: radial-gradient(circle at 35% 35%, #f5a14a 0%, #e2502a 45%, #c41f22 100%);
    border-radius: 50% 50% 50% 50% / 40% 40% 60% 60%;
  }

  .label__brand,
  .label__variety,
  .label__origin,
  .label__abv,
  .label__volume {
    position: absolute;
    margin: 0;
    line-height: 1;
    white-space: nowrap;
  }
  .label__brand,
  .label__variety,
  .label__origin,
  .label__abv {
    left: 0;
    right: 0;
    text-align: center;
  }
  .label__brand {
    top: 241px;
    font-family: "Cinzel", Georgia, serif;
    font-weight: 700;
    font-size: 25px;
    color: var(--title);
  }
  .label__variety {
    top: 282px;
    font-size: 16px;
    letter-spacing: 0.3px;
  }
  .label__origin {
    top: 326px;
    font-size: 21px;
    letter-spacing: 0.5px;
  }
  .label__abv {
    top: 360px;
    font-size: 14px;
  }
  .label__abv small {
    display: block;
    margin-top: 2px;
    font-size: 10.5px;
  }
  .label__volume {
    left: 13px;
    top: 372px;
    font-size: 15px;
  }
</style>
</head>
<body>
<main class="board">

  <section class="label label--pear">
    <div class="label__fruit" role="img" aria-label="Illustration of a ripe yellow pear with a leaf"></div>
    <h2 class="label__brand">VELĒRA CIDER</h2>
    <div class="label__variety">PREMIUM PEAR CIDER</div>
    <div class="label__origin">MADE IN TASMANIA</div>
    <div class="label__volume">330 ml</div>
    <div class="label__abv">4.5%<small>ALC/VOL</small></div>
  </section>

  <section class="label label--apple">
    <div class="label__fruit" role="img" aria-label="Illustration of a green apple with a leaf"></div>
    <h2 class="label__brand">VELĒRA CIDER</h2>
    <div class="label__variety">PREMIUM APPLE CIDER</div>
    <div class="label__origin">MADE IN TASMANIA</div>
    <div class="label__volume">330 ml</div>
    <div class="label__abv">4.5%<small>ALC/VOL</small></div>
  </section>

  <section class="label label--strawberry">
    <div class="label__fruit" role="img" aria-label="Illustration of a red strawberry with green leaves"></div>
    <h2 class="label__brand">VELĒRA CIDER</h2>
    <div class="label__variety">PREMIUM STRAWBERRY CIDER</div>
    <div class="label__origin">MADE IN TASMANIA</div>
    <div class="label__volume">330 ml</div>
    <div class="label__abv">4.5%<small>ALC/VOL</small></div>
  </section>

</main>
</body>
</html>
```